Design for Torvel Ginger Chewy Candy!

Hello! We are Torvel Enterprises Corp, a food manufacturer and distributor based in Los Angeles, CA. We manufacture Chips, Cookies, Juices, Dairy, and last but not least, Candies! We are launching our Ginger Chewy Candy soon and we need a great design for it!

Our Ginger Chewy Candy is a perfect mixture between sweet and spicy from the ginger itself. Torvel Ginger Chewy Candy a good relief for sore throat and nausea.

Now, other than a great design, we also welcome brand suggestions for the candy.
If you can come up with a logo for the Ginger Candy, that would be swell!

We are open to unique and out of the box design. We chose a few color schemes for the design, but feel free to step out of the box if you feel it suits the brand.

We don't have the exact size for the plastic pouch, but it should be a generic small plastic pouch size (approximately 4 oz resealable plastic pouch)

Please have fun designing the project, we can't wait to see all the great designs!

Cheers!

Target Market(s)

USA and Asian market
Age 30-70
Male and Female

Industry/Entity Type

Manufacture

Font styles to use
Serif
Sans Serif
Decorative

Colors
fff3d1
fee18a
fece3e
fbc994
fce8d3

Requirements
Must have
• Torvel Logo
• A picture of ginger (illustrations or photographs are welcome)
Nice to have
• Coating suggestions like Matte surface or SPOT UV
• Give us ideas of what the name of the chewy candy should be. Product name ideas are welcome!

```html
<!DOCTYPE html>
<html lang="en">
<head>
<meta charset="utf-8">
<title>Torvel Ginger Chewy Candy – Pouch Front</title>
<link rel="stylesheet" href="https://fonts.googleapis.com/css2?family=Amatic+SC:wght@700&display=swap">
<style>
  :root {
    --backdrop: #e9e9e7;
    --pouch-top: #f0a02a;
    --pouch-mid: #f4b13c;
    --pouch-bottom: #f9c75c;
    --band-deep: #fbd34e;
    --band-light: #fee18a;
    --band-pale: #fff3d1;
    --brand-blue: #2c3a9c;
    --title-green: #2f7a33;
    --ginger-gold: #f5d364;
    --ginger-rim: #d99a5c;
    --leaf-green: #5aa53f;
    --badge-dark: #3a3a3a;
    --badge-text: #f1c15a;
  }
  * { margin: 0; padding: 0; box-sizing: border-box; }
  html, body { width: 1200px; height: 1200px; overflow: hidden; }
  body {
    background: var(--backdrop);
    position: relative;
    font-family: "Amatic SC", sans-serif;
  }
  .pouch {
    position: absolute;
    left: 320px; top: 120px;
    width: 560px; height: 956px;
    border-radius: 26px 26px 6px 6px;
    background: linear-gradient(160deg, var(--pouch-top) 0%, var(--pouch-mid) 55%, var(--pouch-bottom) 100%);
    overflow: hidden;
  }
  .top-band {
    position: absolute; left: 0; top: 0;
    width: 100%; height: 143px;
    background: linear-gradient(90deg, var(--band-deep) 0%, var(--band-light) 25%, var(--band-pale) 55%, var(--band-light) 80%, var(--band-deep) 100%);
  }
  .brand-name {
    position: absolute;
    top: 168px; left: 0; width: 100%;
    text-align: center;
    font-family: "Amatic SC", sans-serif;
    font-weight: 700;
    font-size: 150px;
    line-height: 1;
    color: var(--brand-blue);
  }
  .product-title {
    position: absolute;
    top: 352px; left: 10px; width: 100%;
    text-align: center;
    font-family: "Amatic SC", sans-serif;
    font-weight: 700;
    font-size: 118px;
    letter-spacing: -3px;
    line-height: 0.93;
    color: var(--title-green);
  }
  .ginger-art {
    position: absolute;
    left: 117px; top: 608px;
    width: 340px; height: 230px;
    border-radius: 40px;
    background: linear-gradient(200deg, var(--leaf-green) 0%, var(--ginger-gold) 45%, #efc458 70%, var(--ginger-rim) 100%);
  }
  .tasty-badge {
    position: absolute;
    left: 165px; top: 855px;
    width: 226px; height: 57px;
    background: var(--badge-dark);
    clip-path: polygon(4% 15%, 100% 0, 96% 85%, 0 100%);
    text-align: center;
    font-family: "Amatic SC", sans-serif;
    font-weight: 700;
    font-size: 46px;
    line-height: 57px;
    color: var(--badge-text);
  }
</style>
</head>
<body>
  <main class="pouch">
    <div class="top-band" role="img" aria-label="Striped shop-awning pattern in pale yellow tones"></div>

    <h1 class="brand-name">Torvel</h1>

    <h2 class="product-title">GINGER CHEWY<br>CANDY</h2>

    <div class="ginger-art" role="img" aria-label="Illustration of glossy golden ginger candy slices with green leaves"></div>

    <div class="tasty-badge">TASTY</div>
  </main>
</body>
</html>
```